Placing my newer logo on my existing business card

I have a business card that I had you guys do years ago, then I changed my logo, I love both my business card and my logo. The challenge is both my logo and my business card are very similar in color. So I'm not sure how to make my logo stand out.

Sick

```html
<!DOCTYPE html>
<html lang="en">
<head>
<meta charset="utf-8">
<title>Alder Creek Health – Business Card Set</title>
<link rel="stylesheet" href="https://fonts.googleapis.com/css2?family=Tinos:wght@400;700&family=Cinzel:wght@500&family=Great+Vibes&display=swap">
<style>
  :root {
    --backdrop: #d2d3d5;
    --card: #ffffff;
    --rust: #a9503a;
    --teal: #86a8aa;
    --ink: #111111;
    --bullet: #6a70b0;
    --photo-top: #c9b5a2;
    --photo-bottom: #8e7464;
  }
  * { margin: 0; padding: 0; box-sizing: border-box; }
  html, body { width: 1200px; height: 960px; overflow: hidden; background: var(--backdrop); }
  body { position: relative; font-family: "Tinos", "Times New Roman", serif; color: var(--ink); }

  .card { position: absolute; width: 395px; height: 231px; background: var(--card); overflow: hidden; }
  .card--front { left: 184px; top: 229px; }
  .card--appointment { left: 621px; top: 229px; }
  .card--director { left: 184px; top: 501px; }
  .card--conditions { left: 621px; top: 501px; }

  .bands { position: absolute; inset: 0; width: 100%; height: 100%; z-index: 2; pointer-events: none; }
  .band-top { fill: var(--rust); }
  .band-bottom { fill: var(--teal); }

  .line { position: absolute; white-space: nowrap; }
  .center { text-align: center; }

  .brand-mark { position: absolute; border-radius: 50%; background: var(--teal); }
  .brand-name { position: absolute; font-family: "Tinos", "Times New Roman", serif; font-weight: 700; color: var(--ink); text-align: center; white-space: nowrap; line-height: 1.1; }

  .label { color: var(--rust); }
  .contact { font-size: 10.5px; }

  .appointment-title { font-family: "Cinzel", serif; font-weight: 500; font-size: 12px; letter-spacing: 0.3px; }
  .fill-row { position: absolute; left: 33px; top: 125px; width: 330px; display: flex; align-items: flex-end; font-size: 9.5px; gap: 5px; }
  .fill-row .rule { border-bottom: 0.8px solid var(--ink); height: 1px; margin-bottom: 2px; }
  .tagline { font-family: "Great Vibes", cursive; font-size: 22px; }

  .person-name { font-weight: 700; font-size: 19px; }
  .person-role { font-size: 9.5px; color: var(--rust); }
  .portrait { position: absolute; left: 274px; top: 0; width: 121px; height: 231px; background: linear-gradient(180deg, var(--photo-top), var(--photo-bottom)); }

  .conditions-title { font-weight: 700; font-size: 12.5px; }
  .condition-list { position: absolute; list-style: none; font-size: 9.4px; line-height: 12.4px; }
  .condition-list li { position: relative; padding-left: 12px; }
  .condition-list li::before { content: ""; position: absolute; left: 0; top: 3.5px; width: 5px; height: 5px; border-radius: 50%; background: var(--bullet); }
  .divider { position: absolute; left: 31px; top: 173px; width: 333px; border-top: 1px solid var(--ink); }
  .call { font-size: 16px; }
</style>
</head>
<body>

<section class="card card--front">
  <svg class="bands" viewBox="0 0 395 231" aria-hidden="true">
    <polygon class="band-top" points="0,0 395,0 395,2 0,12"/>
    <polygon class="band-bottom" points="0,231 395,231 395,219 0,229"/>
  </svg>
  <div class="brand-mark" style="left:112px;top:38px;width:20px;height:20px;"></div>
  <div class="brand-name" style="left:0;top:80px;width:244px;font-size:16px;">Alder Creek Health Center</div>
  <div class="line center contact" style="left:0;top:126px;width:244px;"><span class="label">PH</span>: (555) 014-2270 &nbsp;|&nbsp; <span class="label">FX</span>: (555) 014-2271</div>
  <div class="line center contact" style="left:0;top:143px;width:244px;">aldercreekhealth.com</div>
  <div class="line center contact" style="left:0;top:156px;width:244px;">•</div>
  <div class="line center contact" style="left:0;top:172px;width:244px;">1480 Alder Ave ste#5</div>
  <div class="line center contact" style="left:0;top:188px;width:244px;">north ridge ut 84000</div>
</section>

<section class="card card--appointment">
  <svg class="bands" viewBox="0 0 395 231" aria-hidden="true">
    <polygon class="band-top" points="0,0 395,0 395,2 0,12"/>
    <polygon class="band-bottom" points="0,231 395,231 395,219 0,229"/>
  </svg>
  <div class="brand-mark" style="left:190px;top:22px;width:14px;height:14px;"></div>
  <div class="brand-name" style="left:0;top:45px;width:395px;font-size:9.5px;">Alder Creek Health Center</div>
  <div class="line center appointment-title" style="left:0;top:73px;width:395px;">APPOINTMENT ON....</div>
  <div class="fill-row">
    <span>Time</span><span class="rule" style="width:124px;"></span>
    <span style="margin-left:2px;">Date</span><span class="rule" style="width:150px;"></span>
  </div>
  <div class="line center tagline" style="left:0;top:176px;width:395px;">Let's Make it Happen</div>
</section>

<section class="card card--director">
  <svg class="bands" viewBox="0 0 395 231" aria-hidden="true">
    <polygon class="band-top" points="0,0 395,0 395,2 0,12"/>
    <polygon class="band-bottom" points="0,231 395,231 395,219 0,229"/>
  </svg>
  <div class="portrait" role="img" aria-label="Portrait photo of the director in a white coat against a brick wall"></div>
  <div class="brand-mark" style="left:127px;top:38px;width:18px;height:18px;"></div>
  <div class="brand-name" style="left:0;top:74px;width:272px;font-size:14px;">Alder Creek Health Center</div>
  <div class="line center person-name" style="left:0;top:100px;width:272px;">Marlene Hadley</div>
  <div class="line center person-role" style="left:0;top:123px;width:272px;">Director</div>
  <div class="line center contact" style="left:0;top:142px;width:272px;">1480 Alder Ave ste#5</div>
  <div class="line center contact" style="left:0;top:156px;width:272px;">north Ridge Utah 84000</div>
  <div class="line center contact" style="left:0;top:178px;width:272px;">1(555)014-2270</div>
  <div class="line center contact" style="left:0;top:192px;width:272px;">www.aldercreekhealth.com</div>
</section>

<section class="card card--conditions">
  <svg class="bands" viewBox="0 0 395 231" aria-hidden="true">
    <polygon class="band-top" points="0,0 395,0 395,2 0,12"/>
    <polygon class="band-bottom" points="0,231 395,231 395,219 0,229"/>
  </svg>
  <div class="line center conditions-title" style="left:0;top:14px;width:395px;">Conditions we address for women and men</div>
  <ul class="condition-list" style="left:31px;top:32px;">
    <li>PCOS</li><li>Hysterectomy</li><li>Type-II Diabetes</li><li>Insulin Resistance</li>
    <li>Hypothyroid</li><li>Underactive Thyroid</li><li>Fibromyalgia</li><li>Chronic Fatigue</li>
    <li>Chronic Headaches &amp; Migraines</li><li>Hypertension</li><li>Elevated Fasting Glucose</li>
  </ul>
  <ul class="condition-list" style="left:234px;top:32px;">
    <li>Pre-Diabetes</li><li>Abdominal Obesity</li><li>High Triglycerides</li><li>High Blood Pressure</li>
    <li>High Cholesterol</li><li>Gestational Diabetes</li><li>Epstein Bar</li><li>Infertility</li>
    <li>Infertility Drugs</li><li>Anti-Depression Medications</li>
  </ul>
  <div class="divider"></div>
  <div class="brand-mark" style="left:94px;top:181px;width:11px;height:11px;"></div>
  <div class="brand-name" style="left:52px;top:196px;width:96px;font-size:7.5px;">Alder Creek Health Center</div>
  <div class="line call" style="left:151px;top:180px;">Call Today!: (555)014-2270</div>
  <div class="line contact" style="left:152px;top:198px;">www.aldercreekhealth.com</div>
</section>

</body>
</html>
```